Business Card Design Project

A double sided business card for presentation to business leaders in corporate.

Target Market(s)

Corporate, business professionals, HR

Industry/Entity Type

Business

Requirements
Must have
• FRONT

Logo

www.brightfernco.com.au

BACK

Maren Tollvey-Hart
Director

+ 61 (0) 418 556 230
maren@brightfernco.com.au
www.brightfernco.com.au

Impact through energy and employee engagement

("ripples" of logo, bottom corner)

Must be:
- double sided
size: 86 x 54mm
supplied as one pdf with crop marks shown (+- 1mm, with 2-3 mm bleed)

```html
<!DOCTYPE html>
<html lang="en">
<head>
<meta charset="utf-8">
<title>Bright Fern Co – Business Card</title>
<link href="https://fonts.googleapis.com/css2?family=Arimo:wght@400;700&family=Comfortaa:wght@400;700&display=swap" rel="stylesheet">
<style>
  :root {
    --backdrop: #e3e3e3;
    --plum: #6e1c5a;
    --plum-light: #85306f;
    --plum-deep: #4f0f40;
    --charcoal: #3c3c3c;
    --ink: #2e2e2e;
    --paper: #fbfbfb;
    --white: #ffffff;
  }
  * { box-sizing: border-box; margin: 0; padding: 0; }
  html, body {
    width: 1200px; height: 900px; overflow: hidden;
    background: var(--backdrop);
  }
  .canvas {
    width: 1200px; height: 900px;
    display: flex; align-items: center; justify-content: center; gap: 56px;
  }
  .card {
    position: relative;
    width: 516px; height: 324px;
    overflow: hidden;
    box-shadow: 0 6px 18px rgba(0,0,0,0.18);
  }

  /* Front side */
  .card--front {
    background: radial-gradient(ellipse at 55% 40%, var(--plum-light) 0%, var(--plum) 50%, var(--plum-deep) 100%);
    color: var(--white);
  }
  .front-brand {
    position: absolute; left: 0; right: 0; top: 118px;
    display: flex; align-items: center; justify-content: center; gap: 12px;
  }
  .brand-dot {
    width: 38px; height: 38px; border-radius: 50%;
    background: var(--white);
  }
  .brand-name {
    font-family: "Comfortaa", sans-serif; font-weight: 400;
    font-size: 34px; letter-spacing: 0.5px;
  }
  .front-url {
    position: absolute; left: 0; right: 0; bottom: 92px;
    text-align: center;
    font-family: "Arimo", sans-serif; font-size: 11px; letter-spacing: 0.4px;
  }

  /* Back side */
  .card--back { background: var(--paper); color: var(--ink); }
  .back-brand {
    position: absolute; right: 56px; top: 50px;
    display: flex; align-items: center; gap: 10px;
  }
  .card--back .brand-dot { width: 30px; height: 30px; background: var(--plum); }
  .card--back .brand-name { font-size: 30px; color: var(--ink); }
  .contact {
    position: absolute; right: 40px; top: 118px;
    list-style: none;
    font-family: "Arimo", sans-serif; font-size: 11px; line-height: 17px;
    text-align: right; color: var(--ink);
  }
  .contact li { display: flex; align-items: center; justify-content: flex-end; gap: 6px; }
  .contact svg { width: 11px; height: 11px; flex: none; }
  .holder {
    position: absolute; left: 34px; top: 208px;
    font-family: "Arimo", sans-serif;
  }
  .holder-name { font-weight: 700; font-size: 17px; color: var(--ink); }
  .holder-role { font-size: 12px; margin-top: 3px; color: var(--ink); }
  .marker { position: absolute; left: 36px; bottom: 14px; width: 12px; height: 10px; }
  .corner-feature {
    position: absolute; left: 270px; right: 0; bottom: 0; height: 70px;
    background: linear-gradient(90deg, var(--plum) 0%, var(--charcoal) 100%);
  }
</style>
</head>
<body>
<main class="canvas">
  <section class="card card--front" aria-label="Card front">
    <div class="front-brand">
      <span class="brand-dot"></span>
      <span class="brand-name">Bright Fern Co</span>
    </div>
    <p class="front-url">www.brightfernco.com.au</p>
  </section>

  <section class="card card--back" aria-label="Card back">
    <div class="corner-feature" role="img" aria-label="Decorative ripple bands in plum and charcoal"></div>
    <div class="back-brand">
      <span class="brand-dot"></span>
      <span class="brand-name">Bright Fern Co</span>
    </div>
    <ul class="contact">
      <li>+ 61 (0) 418 556 230
        <svg viewBox="0 0 12 12" aria-hidden="true"><path fill="var(--ink)" d="M1 3 C1 1.5 3 1 6 1 C9 1 11 1.5 11 3 L9 4 L8 3 L4 3 L3 4 Z M3 5 L9 5 L10 11 L2 11 Z"/></svg></li>
      <li>maren@brightfernco.com.au
        <svg viewBox="0 0 12 12" aria-hidden="true"><rect x="1" y="2.5" width="10" height="7" fill="none" stroke="var(--ink)" stroke-width="1.2"/><path d="M1 2.5 L6 7 L11 2.5" fill="none" stroke="var(--ink)" stroke-width="1.2"/></svg></li>
      <li>www.brightfernco.com.au
        <svg viewBox="0 0 12 12" aria-hidden="true"><circle cx="6" cy="6" r="5" fill="none" stroke="var(--ink)" stroke-width="1.2"/><ellipse cx="6" cy="6" rx="2.2" ry="5" fill="none" stroke="var(--ink)" stroke-width="1"/><path d="M1 6 H11" stroke="var(--ink)" stroke-width="1"/></svg></li>
    </ul>
    <div class="holder">
      <p class="holder-name">Maren Tollvey-Hart</p>
      <p class="holder-role">Director</p>
    </div>
    <svg class="marker" viewBox="0 0 12 10" aria-hidden="true"><path d="M0 10 L6 0 L12 10 Z" fill="var(--ink)"/></svg>
  </section>
</main>
</body>
</html>
```